Web Design Project - wine stock exchange

This page shall be informative about Vinery Hall to express their values. And, like the normal stock exchanges, clients can bid and ask for price indications.
Also, the clients can generate their own wines like the winemakers provide individual barrowls to design by the clients.

```html
<!DOCTYPE html>
<html lang="en">
<head>
<meta charset="utf-8">
<title>Cask &amp; Bid – Online Wine Auctions</title>
<link href="https://fonts.googleapis.com/css2?family=Cinzel:wght@400;700&family=Open+Sans:wght@400;700&display=swap" rel="stylesheet">
<style>
:root{
  --backdrop:#3b3b3b;
  --paper:#ffffff;
  --cream:#fbf6e4;
  --wine-green:#1f4a1c;
  --btn-green:#123d10;
  --ribbon:#c8102e;
  --nav-tan:#cf9a55;
  --nav-line:#a9763a;
  --search-red:#b3112c;
  --mint:#a6e3d2;
  --charcoal:#333333;
  --orange:#fb9b32;
  --card-light:#c98b48;
  --card-dark:#a9651b;
  --gold:#ffe23a;
  --ink:#222222;
  --footer-peach:#fcc898;
}
*{box-sizing:border-box;margin:0;padding:0}
html,body{width:1200px;height:900px;overflow:hidden}
body{background:var(--backdrop);font-family:"Open Sans",Tahoma,sans-serif;color:var(--ink);position:relative}
.page{position:absolute;left:332px;top:0;width:563px;height:900px;background:var(--cream)}
.abs{position:absolute}

/* header */
.site-header{left:0;top:0;width:563px;height:100px;background:linear-gradient(180deg,#fff 0%,#f6f3e2 100%)}
.ribbon{left:-30px;top:14px;width:150px;height:20px;background:var(--ribbon);color:#fff;font-size:9px;font-weight:700;text-align:center;line-height:20px;transform:rotate(-45deg);transform-origin:center}
.ribbon-clip{left:0;top:0;width:90px;height:90px;overflow:hidden}
.brand{left:60px;top:30px;font-family:"Cinzel",serif;font-weight:400;font-size:30px;color:var(--wine-green);letter-spacing:1px}
.top-btn{top:20px;height:18px;background:var(--btn-green);color:#fff;font-size:11px;line-height:18px;padding:0 6px;border:1px solid #0a2a08}
.vine{left:360px;top:10px;width:200px;height:92px;background:radial-gradient(ellipse at 55% 50%,#7cc22a 0%,#b7dc6a 45%,rgba(251,246,228,0) 75%)}

/* nav */
.main-nav{left:0;top:100px;width:563px;height:198px;background:var(--nav-tan);display:flex}
.nav-item{flex:1;border-right:2px solid var(--nav-line);position:relative;color:#1a1a1a}
.nav-item:last-child{border-right:0}
.nav-photo{position:absolute;left:8px;top:8px;width:125px;height:146px;border:2px solid #fff;background:linear-gradient(160deg,#6b5a45,#2a2018 70%)}
.nav-photo.blog{background:linear-gradient(90deg,#8b0c12,#c0141c 50%,#8b0c12)}
.nav-photo.sell{background:linear-gradient(160deg,#e8e8e0,#2f3f18 60%)}
.nav-label{position:absolute;left:0;right:0;top:164px;text-align:center;font-family:"Cinzel",serif;font-size:16px}

/* left column */
.search{left:1px;top:308px;width:185px;height:30px;background:var(--search-red);color:#fff;font-size:8px;font-weight:700;display:flex;align-items:center;gap:5px;padding-left:8px}
.search-field{width:91px;height:12px;background:#f3dce0}
.intro{left:2px;top:353px;width:184px;height:115px;background:var(--mint);font-size:7.2px;font-weight:700;line-height:9px;padding:8px 9px;color:#1b2a33}
.intro p{margin-bottom:9px}
.intro .hl{color:var(--search-red)}
.intro u{color:var(--search-red)}
.winners-head{left:1px;top:470px;width:185px;height:36px;background:var(--charcoal);color:#fff;font-family:"Cinzel",serif;font-size:17px;text-align:center;line-height:36px}
.winners{left:1px;top:506px;width:185px;height:256px;background:var(--orange)}
.winner{position:absolute;left:0;width:185px;height:58px;border-bottom:1px solid #f7b56a}
.avatar{position:absolute;left:8px;top:8px;width:44px;height:48px;background:linear-gradient(180deg,#c9a078,#23334a);border-radius:4px}
.winner p{position:absolute;left:58px;top:8px;width:122px;font-size:6.5px;line-height:9px;color:#332}
.winner b{color:#6b1a00}
.more{right:10px;bottom:8px;font-size:7px;font-weight:700;color:#333}

/* what's new */
.new-head{left:194px;top:306px;width:367px;height:30px;background:var(--charcoal);color:#fff}
.new-head h2{position:absolute;left:9px;top:3px;font-family:"Cinzel",serif;font-weight:400;font-size:17px}
.new-head a{position:absolute;right:16px;top:11px;font-size:7px;font-weight:700;color:#fff;text-decoration:none}
.card{position:absolute;width:176px;height:131px;background:var(--card-light);border:1px solid #b07b40}
.card.dark{background:var(--card-dark)}
.card .bottle{position:absolute;left:0;top:0;width:63px;height:129px;background:#fff}
.card .bottle i{position:absolute;left:24px;top:14px;width:16px;height:100px;border-radius:6px 6px 3px 3px;background:linear-gradient(180deg,#3a0c0c,#1a0606)}
.card .info{position:absolute;left:68px;top:8px;width:105px;color:#fff;font-size:7.5px;line-height:10px}
.card h3{font-size:8px;font-weight:700;line-height:10px;margin-bottom:6px}
.card .was{margin-left:2px;margin-bottom:10px;color:#222}
.card .note{margin-left:2px;color:#222;margin-bottom:12px}
.card .price{margin-left:2px;color:var(--gold);font-weight:700}
.bid{position:absolute;left:72px;bottom:6px;background:#fff;color:#111;font-size:8px;font-weight:700;padding:2px 5px;box-shadow:2px 2px 0 #553}
.closed{position:absolute;left:0;top:49px;width:174px;height:34px;background:rgba(60,60,60,.85);color:#fff;font-size:13px;text-align:center;line-height:34px}

/* footer */
.site-footer{left:1px;top:767px;width:561px;height:104px;background:#fff;border:1px solid #555}
.fcol{position:absolute;top:6px}
.fcol h4{font-family:"Cinzel",serif;font-weight:400;font-size:12px;margin-bottom:4px;color:#222}
.fcol li{list-style:none;font-size:7px;line-height:11.4px;color:#111}
.fsep{position:absolute;top:16px;width:1px;height:74px;background:#bbb}
.bottom-bar{left:0;top:875px;width:563px;height:25px;background:var(--footer-peach);font-size:8px;line-height:21px;text-align:right;padding-right:18px;color:#222}
</style>
</head>
<body>
<div class="page">
  <header class="site-header abs">
    <div class="vine abs" role="img" aria-label="Green grape vine leaves"></div>
    <div class="ribbon-clip abs"><div class="ribbon abs">Online Wine Auctions</div></div>
    <div class="brand abs">CASK &amp; BID</div>
    <a class="top-btn abs" style="left:302px">Login</a>
    <a class="top-btn abs" style="left:354px">CONTACT</a>
  </header>

  <nav class="main-nav abs">
    <div class="nav-item"><div class="nav-photo" role="img" aria-label="Three aged wine bottles before a wooden crate"></div><span class="nav-label">HOME</span></div>
    <div class="nav-item"><div class="nav-photo" role="img" aria-label="Rows of wine bottle necks"></div><span class="nav-label">BUY WINE</span></div>
    <div class="nav-item"><div class="nav-photo sell" role="img" aria-label="Three green-labelled wine bottles"></div><span class="nav-label">SELL WINE</span></div>
    <div class="nav-item"><div class="nav-photo blog" role="img" aria-label="A single wine bottle before a red curtain"></div><span class="nav-label">BLOG</span></div>
  </nav>

  <div class="search abs">Find Wine : <span class="search-field"></span> <span style="margin-left:4px">Search</span></div>

  <div class="intro abs">
    <p>Online wine auction site Cask &amp; Bid offers a trading platform to buy and serare and vintage fine wines via real-time auctions.</p>
    <p>See our guide on how to <span class="hl">sell wine</span> at auction using Cask &amp; Bid, request a valuation or start <u>buying or selling</u> now.</p>
    <p>To hear the latest news and receive up to the minute information on newly offered wines, why not follow us on Chirper or subscre to our blog?</p>
  </div>

  <div class="winners-head abs">Happy Winners</div>
  <div class="winners abs">
    <div class="winner" style="top:0"><div class="avatar" role="img" aria-label="Winner avatar"></div><p><b>Lena Marsh</b> Auction is one of the most incredbe concepts conceived in e-commerce and offers an absorbig online gaming activty supported by</p></div>
    <div class="winner" style="top:62px"><div class="avatar" role="img" aria-label="Winner avatar"></div><p><b>Lena Marsh</b> Auction is one of the most incredbe concepts conceived in e-commerce</p></div>
    <div class="winner" style="top:124px"><div class="avatar" role="img" aria-label="Winner avatar"></div><p><b>Lena Marsh</b> Auction is one of the most incredbe concepts conceived in e-commerce and offers an absorbig online gaming activty supported by</p></div>
    <div class="winner" style="top:186px;border:0"><div class="avatar" role="img" aria-label="Winner avatar"></div><p><b>Lena Marsh</b> Auction is one of the most incredbe concepts conceived in e-commerce</p></div>
    <span class="more abs">more &gt;&gt;</span>
  </div>

  <div class="new-head abs"><h2>What's New Here?</h2><a>View all &gt;&gt;</a></div>

  <div class="card" style="left:193px;top:341px"><div class="bottle" role="img" aria-label="Red wine bottle"><i></i></div>
    <div class="info"><h3>Chateau Valmorent</h3><p class="was">Save £30 Was £85.44</p><p class="note">Fantastically elegant with great finesse</p><p class="price">MRP: 699.00/-<br>Last Sold: Rs. 0.33</p></div><span class="bid">BID NOW</span></div>
  <div class="card dark" style="left:383px;top:341px"><div class="bottle" role="img" aria-label="Dark wine bottle"><i></i></div>
    <div class="info"><h3>Chateau Valmorent 2002 St Emilion France</h3><p class="was">Save £30 Was £85.44</p><p class="note">Fantastically elegant with great finesse</p><p class="price">MRP: 699.00/-<br>Last Sold: Rs. 0.33</p></div><span class="bid">BID NOW</span></div>

  <div class="card" style="left:193px;top:486px"><div class="bottle" role="img" aria-label="Vintage wine bottle"><i></i></div>
    <div class="info"><h3>Chateau Valmorent 2002 St Emilion France</h3><p class="was">Save £30 Was £85.44</p><p class="note">Fantastically elegant with great finesse</p><p class="price">MRP: 699.00/-<br>Last Sold: Rs. 0.33</p></div><span class="bid">BID NOW</span>
    <div class="closed">Action Closed</div></div>
  <div class="card dark" style="left:383px;top:486px"><div class="bottle" role="img" aria-label="Champagne bottle"><i style="background:linear-gradient(180deg,#d8c27a,#2f4a1a 30%)"></i></div>
    <div class="info"><h3>Chateau Valmorent</h3><p class="was">Save £30 Was £85.44</p><p class="note">Fantastically elegant with great finesse</p><p class="price">MRP: 699.00/-<br>Last Sold: Rs. 0.33</p></div><span class="bid">BID NOW</span></div>

  <div class="card" style="left:193px;top:632px"><div class="bottle" role="img" aria-label="Red wine bottle with red capsule"><i style="background:linear-gradient(180deg,#b01818,#3a0c0c 30%)"></i></div>
    <div class="info"><h3>Chateau Valmorent 2002 St Emilion France</h3><p class="was">Save £30 Was £85.44</p><p class="note">Fantastically elegant with great finesse</p><p class="price">MRP: 699.00/-<br>Last Sold: Rs. 0.33</p></div><span class="bid">BID NOW</span></div>
  <div class="card dark" style="left:383px;top:632px"><div class="bottle" role="img" aria-label="Red wine bottle"><i></i></div>
    <div class="info"><h3>Chateau Valmorent 2002 St Emilion France</h3><p class="was">Save £30 Was £85.44</p><p class="note">Fantastically elegant with great finesse</p><p class="price">MRP: 699.00/-<br>Last Sold: Rs. 0.33</p></div><span class="bid">BID NOW</span></div>

  <footer class="site-footer abs">
    <div class="fcol" style="left:112px"><h4>AUCTIONS</h4><ul><li>Time Based</li><li>Bid Based(Limited)</li><li>Pick2Win</li><li>Bid or Buy</li><li>Partner with Us</li></ul></div>
    <div class="fsep" style="left:210px"></div>
    <div class="fcol" style="left:233px"><h4>USEFUL LINKS</h4><ul><li>Register/Login</li><li>Customer support</li><li>100% Refund Policy</li><li>Tips &amp; Tricks to win</li><li>Refer a Friend</li><li>Rewards &amp; Schemes</li></ul></div>
    <div class="fsep" style="left:346px"></div>
    <div class="fcol" style="left:370px"><h4>COMPANY</h4><ul><li>About Us</li><li>Privacy Agreement</li><li>Terms &amp; Conditions</li><li>Contact Us</li><li>Sitemap</li><li>Advertise With Us</li></ul></div>
  </footer>
  <div class="bottom-bar abs">© Copyright 2012 Vinery Hall. All Rights Reserved. &nbsp;&nbsp; Privacy Policy | Terms &amp; Conditions</div>
</div>
</body>
</html>
```